Web tool bar Project

I'm open to paying more if the quality of the bar is very good... if you feel the scope of the project does not match budget..... please quote me.

I need someone to re-design my web tool bar.

In the first attachment you can see a black tool bar (fig1). This is my old design. I want this to be the template as it shows what the text will say and where the buttons will be placed.

For the new tool bar:
-I would like the it to be white in colour (like fig.2)
-I would like the buttons to also be white. But the buttons must stand out so the designer should use the right shading to make the buttons stand out.
-The bar needs to be the quality of the bar in fig.2 (very good quality). I have had many designs done for this but no designer seems to be good enough to get the right quality.
-The text in the white boxes on the new bar should be the colours shown above the buttons next to fig.1 (blue, green, red, yellow, purple & orange).

Finally please put the logo attached (DV) at the end of the bar on the right where it says logo. The logo should blend in well with the bar as it has white in it also.

Please take note of fig.2 it is good quality with sharp edges I would like the same quality.

Any further questions please ask?

Requirements
Must have
• Quality!

```html
<!DOCTYPE html>
<html lang="en">
<head>
<meta charset="utf-8">
<title>Web Toolbar</title>
<link href="https://fonts.googleapis.com/css2?family=Signika:wght@500;600&display=swap" rel="stylesheet">
<style>
  :root {
    --bar-top: #f7f7f7;
    --bar-bottom: #d6d6d6;
    --btn-top: #ffffff;
    --btn-bottom: #ececec;
    --btn-border: #b9b9b9;
    --green: #6b9c1e;
    --red: #c23a2c;
    --yellow: #efb60c;
    --orange: #f26f21;
    --brand-blue: #1a8fe0;
  }
  html, body {
    margin: 0;
    padding: 0;
    width: 1200px;
    height: 80px;
    overflow: hidden;
  }
  .toolbar {
    position: relative;
    width: 1200px;
    height: 80px;
    background: linear-gradient(to bottom, var(--bar-top), var(--bar-bottom));
    font-family: "Signika", "Trebuchet MS", sans-serif;
  }
  .toolbar-btn {
    position: absolute;
    top: 20px;
    height: 40px;
    box-sizing: border-box;
    display: flex;
    align-items: center;
    justify-content: center;
    gap: 7px;
    border: 1px solid var(--btn-border);
    border-radius: 3px;
    background: linear-gradient(to bottom, var(--btn-top), var(--btn-bottom));
    box-shadow: inset 0 1px 0 #fff, 0 1px 2px rgba(0,0,0,0.12);
    font-size: 16px;
    font-weight: 600;
    letter-spacing: 0.1px;
  }
  .toolbar-btn svg { flex: none; }
  .btn-checkin { left: 100px; width: 120px; color: var(--green); }
  .btn-friends { left: 230px; width: 260px; color: var(--red); }
  .btn-feeds { left: 500px; width: 170px; color: var(--yellow); }
  .btn-scrapbook { left: 680px; width: 150px; color: var(--orange); }
  .brand {
    position: absolute;
    left: 1040px;
    top: 10px;
    height: 60px;
    display: flex;
    align-items: center;
    gap: 8px;
  }
  .brand-mark {
    width: 26px;
    height: 26px;
    border-radius: 4px;
    background: var(--brand-blue);
  }
  .brand-name {
    font-size: 28px;
    font-weight: 500;
    color: var(--brand-blue);
  }
</style>
</head>
<body>
<div class="toolbar">
  <div class="toolbar-btn btn-checkin">
    <svg width="12" height="16" viewBox="0 0 12 16" aria-hidden="true">
      <path d="M6 0C2.7 0 0 2.6 0 5.9 0 10 6 16 6 16s6-6 6-10.1C12 2.6 9.3 0 6 0zm0 8.3A2.4 2.4 0 1 1 6 3.5a2.4 2.4 0 0 1 0 4.8z" fill="currentColor"/>
    </svg>
    <span>Check In</span>
  </div>
  <div class="toolbar-btn btn-friends">
    <svg width="22" height="16" viewBox="0 0 22 16" aria-hidden="true">
      <circle cx="7" cy="4" r="3.6" fill="currentColor"/>
      <path d="M0 16c0-4.4 3-7 7-7s7 2.6 7 7z" fill="currentColor"/>
      <circle cx="15" cy="5" r="3" fill="currentColor"/>
      <path d="M15 9.5c3.6 0 6 2.2 6 6.5h-5.5c0-2.6-0.9-4.8-2.8-6.3 0.7-0.1 1.5-0.2 2.3-0.2z" fill="currentColor"/>
    </svg>
    <span>Online Friends at Orbitnet</span>
  </div>
  <div class="toolbar-btn btn-feeds">
    <svg width="14" height="14" viewBox="0 0 14 14" aria-hidden="true">
      <circle cx="2" cy="12" r="2" fill="currentColor"/>
      <path d="M0 5.5a8.5 8.5 0 0 1 8.5 8.5" stroke="currentColor" stroke-width="2" fill="none"/>
      <path d="M0 1a13 13 0 0 1 13 13" stroke="currentColor" stroke-width="2" fill="none"/>
    </svg>
    <span>Lounge Feeds</span>
  </div>
  <div class="toolbar-btn btn-scrapbook">
    <svg width="20" height="16" viewBox="0 0 20 16" aria-hidden="true">
      <path d="M10 5 C7 3 4 3 1.5 4.5 L4 14 C6 13 8 13 10 14.5 C12 13 14 13 16 14 L18.5 4.5 C16 3 13 3 10 5 Z M10 5 L10 14.5" stroke="currentColor" stroke-width="1.5" fill="none" stroke-linejoin="round"/>
    </svg>
    <span>Scrapbook</span>
  </div>
  <div class="brand">
    <span class="brand-mark"></span>
    <span class="brand-name">DV</span>
  </div>
</div>
</body>
</html>
```